New website

Our website (www.larchhollow.com) needs to be replaced with something gorgeous and glossy. We do like the text of our current website but have many new images to put on the site. We want to create a website that shows viewers what our team can do, and how we can create something amazing for them and their homes.

Coding

```html
<!DOCTYPE html>
<html lang="en">
<head>
<meta charset="utf-8">
<title>Larch Hollow Landscaping</title>
<link href="https://fonts.googleapis.com/css2?family=Lexend:wght@400;500;600&family=Poppins:wght@400;500;600&family=Archivo:wght@600;700&family=Zilla+Slab:wght@700&family=Cormorant+Garamond:wght@500&display=swap" rel="stylesheet">
<style>
:root{
  --green:#3fb55c;
  --green-dark:#2f9a4a;
  --blue:#2f82d0;
  --blue-light:#b9d9f3;
  --ink:#1d1d1d;
  --muted:#444;
  --forest:#13241a;
  --forest-2:#1f3a25;
  --white:#fff;
  --line:#d8d8d8;
}
*{margin:0;padding:0;box-sizing:border-box}
html,body{width:1200px;height:3812px;overflow:hidden;background:#fff}
body{font-family:"Poppins",sans-serif;color:var(--ink)}
.page{position:relative;width:1200px;height:3812px;overflow:hidden}
.abs{position:absolute}
.btn{position:absolute;display:flex;align-items:center;justify-content:center;background:var(--green);color:#fff;border-radius:22px;font:500 12px "Poppins",sans-serif}
.h2{position:absolute;left:0;width:1200px;text-align:center;font:600 33px "Lexend",sans-serif;color:var(--green)}
.wordmark{font:500 30px "Cormorant Garamond",serif;letter-spacing:5px;color:#2a3b35;text-transform:uppercase}

/* header */
.site-header{left:0;top:0;width:1200px;height:75px;background:#fff}
.site-header .wordmark{position:absolute;left:74px;top:20px}
.nav a{position:absolute;top:29px;font:400 12px "Poppins",sans-serif;color:var(--ink);text-decoration:none}
.nav a.active{color:var(--green);border-bottom:1px solid var(--green);padding-bottom:2px}
.icon-circle{position:absolute;border-radius:50%;display:flex;align-items:center;justify-content:center}
.call small{display:block;font-size:8px;color:#888}
.call b{font:600 12px "Poppins",sans-serif}

/* hero */
.hero{left:0;top:75px;width:1200px;height:525px;background:linear-gradient(100deg,#1d4a1e 0%,#2f6a25 35%,#4c8b33 60%,#2d5a24 100%)}
.hero h1{position:absolute;left:0;top:178px;width:1200px;text-align:center;font:700 48px "Zilla Slab",serif;color:#fff;letter-spacing:1px}
.hero p{position:absolute;left:0;top:238px;width:1200px;text-align:center;font:500 11.5px "Poppins",sans-serif;color:#fff}

/* about */
.about-photo{left:157px;top:685px;width:380px;height:375px;border-radius:8px;background:linear-gradient(135deg,#6f9a55,#2f6a35 55%,#9b7a5c)}
.about-accent{left:520px;top:760px;width:24px;height:290px;background:var(--green);border-radius:0 8px 8px 0}
.badge{left:389px;top:903px;width:191px;height:86px;background:var(--blue);border:3px solid #fff;border-radius:10px;box-shadow:0 0 0 2px var(--blue);color:#fff;display:flex;align-items:center;gap:10px;padding-left:22px}
.badge b{font:600 40px "Lexend",sans-serif}
.badge span{font:500 14px/1.1 "Lexend",sans-serif}
.about-text{left:642px;top:690px;width:390px}
.about-text h2{font:600 33px "Lexend",sans-serif;color:var(--green);margin-bottom:22px}
.about-text p{font:400 11.5px/18px "Poppins",sans-serif;color:var(--muted);margin-bottom:23px}
.info-row{left:642px;top:958px;display:flex;gap:24px}
.info{display:flex;align-items:center;gap:7px}
.info .dot{width:32px;height:32px;border-radius:50%;background:#222;display:flex;align-items:center;justify-content:center}
.info small{display:block;font-size:8px;color:#888}
.info b{font:600 11.5px "Poppins",sans-serif}

/* dark bands */
.band{left:0;width:1200px;background:radial-gradient(ellipse at 50% 40%,var(--forest-2),var(--forest) 75%)}
.service-card{position:absolute;width:278px;height:247px;background:#fff;border-radius:8px;border:3px solid #fff;overflow:hidden}
.service-card .thumb{position:absolute;left:0;bottom:0;width:272px;height:172px;border-radius:6px}
.service-card .ic{left:18px;top:8px;width:66px;height:66px;background:var(--green);border:4px solid #fff;z-index:2}
.service-card h3{position:absolute;left:100px;top:20px;font:700 13.5px/17px "Archivo",sans-serif;text-transform:uppercase;color:#111}

/* testimonials */
.quote{left:568px;top:2102px;width:62px;height:62px;background:var(--blue)}
.stars{left:0;top:2176px;width:1200px;text-align:center;color:#f3c210;font-size:18px;letter-spacing:4px}
.t-title{left:0;top:2212px;width:1200px;text-align:center;font:600 11px "Poppins",sans-serif}
.t-body{left:0;top:2231px;width:1200px;text-align:center;font:400 11px/19px "Poppins",sans-serif;color:#333}
.arrow{position:absolute;top:2228px}

/* blog */
.blog-card{position:absolute;top:2540px;width:278px;height:296px;background:#fff;border-radius:8px;border:3px solid #fff}
.blog-card .thumb{position:absolute;left:0;top:0;width:272px;height:170px;border-radius:6px}
.date{left:24px;top:133px;width:66px;height:66px;background:var(--green);border:4px solid #fff;color:#fff;flex-direction:column;font:400 10px "Lexend",sans-serif}
.date b{font:600 15px "Lexend",sans-serif}
.blog-card h3{position:absolute;left:15px;top:202px;width:250px;font:700 12.5px/17px "Archivo",sans-serif;text-transform:uppercase}
.blog-card p{position:absolute;left:15px;top:240px;width:250px;font:400 11px/18px "Poppins",sans-serif;color:#333}

/* form */
.field{position:absolute;border:1px solid var(--line);font:400 10.5px "Poppins",sans-serif;color:#999;padding:10px 12px}

/* footer */
.footer{left:0;top:3543px;width:1200px;height:269px;background:radial-gradient(ellipse at 50% 30%,#24382a,#152219 75%)}
.footer-logo{left:460px;top:3497px;width:280px;height:88px;background:#fff;border-radius:4px;box-shadow:0 2px 8px rgba(0,0,0,.2);display:flex;align-items:center;justify-content:center}
.f-item{position:absolute;top:3648px;display:flex;gap:10px;color:#fff}
.f-item small{display:block;font-size:9px;color:var(--green)}
.f-item b{font:500 11.5px/16px "Poppins",sans-serif}
.f-nav a{position:absolute;top:3736px;font:400 11.5px "Poppins",sans-serif;color:#fff;text-decoration:none}
.bottom-bar{left:0;top:3770px;width:1200px;height:42px;background:#6aa63d;color:#fff;font:400 10.5px "Poppins",sans-serif}
</style>
</head>
<body>
<div class="page">

<!-- header -->
<header class="abs site-header">
  <div class="wordmark">Larch Hollow</div>
  <nav class="nav">
    <a class="active" style="left:450px">Home</a>
    <a style="left:511px">About Us</a>
    <a style="left:588px">Services</a>
    <a style="left:662px">Testimonials</a>
    <a style="left:758px">Contact Us</a>
  </nav>
  <div class="btn" style="left:848px;top:21px;width:147px;height:34px">Get a Free Estimate</div>
  <div class="icon-circle" style="left:1006px;top:21px;width:34px;height:34px;background:var(--green)">
    <svg width="14" height="14" viewBox="0 0 24 24" fill="#fff"><path d="M6.6 10.8a15 15 0 006.6 6.6l2.2-2.2c.3-.3.7-.4 1-.2 1.1.4 2.3.6 3.6.6.6 0 1 .4 1 1V20c0 .6-.4 1-1 1A17 17 0 013 4c0-.6.4-1 1-1h3.5c.6 0 1 .4 1 1 0 1.3.2 2.5.6 3.6.1.3 0 .7-.2 1z"/></svg>
  </div>
  <div class="abs call" style="left:1046px;top:24px"><small>Call Now</small><b>(555) 214-7380</b></div>
</header>

<!-- hero -->
<section class="abs hero" role="img" aria-label="Landscaper in cap and overalls trimming a green hedge with shears">
  <h1>EXPERTS FOR ALL SEASONS</h1>
  <p>MORE THAN JUST LANDSCAPING &amp; SNOW REMOVAL</p>
  <div class="btn" style="left:527px;top:277px;width:146px;height:30px;font-size:11.5px">Get a Free Estimate</div>
</section>
<svg class="abs" style="left:0;top:520px" width="1200" height="90" viewBox="0 0 1200 90">
  <defs><linearGradient id="waveBlue" x1="0" x2="1"><stop offset="0" stop-color="#2f82d0"/><stop offset=".55" stop-color="#4a97dc"/><stop offset="1" stop-color="#c6e0f5"/></linearGradient></defs>
  <path d="M0 10 C 200 70, 380 90, 620 62 S 1000 20, 1200 40 L1200 90 L0 90Z" fill="url(#waveBlue)"/>
  <path d="M0 30 C 200 90, 420 92, 660 72 S 1020 40, 1200 82 L1200 90 L0 90Z" fill="#fff"/>
</svg>

<!-- about -->
<div class="abs about-accent"></div>
<div class="abs about-photo" role="img" aria-label="Gardener in a green apron pruning a potted plant in a nursery"></div>
<div class="abs badge"><b>20</b><span>Years of<br>Experience</span></div>
<div class="abs about-text">
  <h2>About Us</h2>
  <p>Established in 2005 as a way to pay for college tuition, Larch Hollow has instead become our passion. With a garage sale mower and a commitment to doing every job well, our list of satisfied customers grew quickly over the years.</p>
  <p>While the scope of our landscaping company has grown, our way of doing business has not. It is still rooted in the desire to do quality work whether the job includes a simple tree service or the installation of an entire irrigation system, provide exceptional value, and to serve our clients with integrity.</p>
</div>
<div class="abs info-row">
  <div class="info"><div class="dot"><svg width="13" height="13" viewBox="0 0 24 24" fill="#fff"><path d="M6.6 10.8a15 15 0 006.6 6.6l2.2-2.2c.3-.3.7-.4 1-.2 1.1.4 2.3.6 3.6.6.6 0 1 .4 1 1V20c0 .6-.4 1-1 1A17 17 0 013 4c0-.6.4-1 1-1h3.5c.6 0 1 .4 1 1 0 1.3.2 2.5.6 3.6.1.3 0 .7-.2 1z"/></svg></div><div><small>Call Now</small><b>(555) 214-7380</b></div></div>
  <div class="info"><div class="dot"><svg width="14" height="14" viewBox="0 0 24 24"><circle cx="12" cy="12" r="9" fill="#fff"/><path d="M12 7v5l3 2" stroke="#222" stroke-width="2" fill="none"/></svg></div><div><small>Monday-Saturday</small><b>7:00am-7:00pm</b></div></div>
</div>
<div class="btn" style="left:642px;top:1017px;width:95px;height:31px">Read More</div>

<!-- services -->
<section class="abs band" style="top:1135px;height:840px" role="img" aria-label="Darkened photo of a landscaped garden"></section>
<h2 class="h2" style="top:1200px;color:var(--green)">Services</h2>

<div class="service-card" style="left:157px;top:1264px"><div class="icon-circle abs ic"><svg width="30" height="30" viewBox="0 0 24 24" fill="none" stroke="#fff" stroke-width="1.6"><path d="M3 4l4 9h12v4H6"/><circle cx="8" cy="18" r="2"/><circle cx="17" cy="18" r="2"/></svg></div><h3>Lawn<br>Maintenance</h3><div class="thumb" role="img" aria-label="Lawn mower cutting bright green grass" style="background:linear-gradient(180deg,#8fae77,#4d8a2e)"></div></div>
<div class="service-card" style="left:460px;top:1264px"><div class="icon-circle abs ic"><svg width="30" height="30" viewBox="0 0 24 24" fill="none" stroke="#fff" stroke-width="1.6"><path d="M6 3l8 12M18 3l-8 12"/><circle cx="8" cy="19" r="2.5"/><circle cx="16" cy="19" r="2.5"/></svg></div><h3>Landscape<br>Maintenance</h3><div class="thumb" role="img" aria-label="Gloved hands trimming a rounded shrub with shears" style="background:linear-gradient(180deg,#6e8a4c,#8dbb3b)"></div></div>
<div class="service-card" style="left:765px;top:1264px"><div class="icon-circle abs ic"><svg width="30" height="30" viewBox="0 0 24 24" fill="none" stroke="#fff" stroke-width="1.6"><path d="M20 4L9 15M5 14l5 5M4 18l2 2"/></svg></div><h3>Lawn Core<br>Aeration</h3><div class="thumb" role="img" aria-label="Worker aerating soil beside garden plants" style="background:linear-gradient(180deg,#6f8f5a,#3e5a2a)"></div></div>
<div class="service-card" style="left:157px;top:1539px"><div class="icon-circle abs ic"><svg width="30" height="30" viewBox="0 0 24 24" fill="none" stroke="#fff" stroke-width="1.6"><rect x="3" y="9" width="14" height="8" rx="1"/><path d="M17 12h4M6 4v5"/><circle cx="7" cy="19" r="2"/><circle cx="14" cy="19" r="2"/></svg></div><h3>Lawn<br>Fertilization</h3><div class="thumb" role="img" aria-label="Hand using a trowel on dark soil with seedlings" style="background:linear-gradient(180deg,#5a4a38,#2e2418)"></div></div>
<div class="service-card" style="left:460px;top:1539px"><div class="icon-circle abs ic"><svg width="30" height="30" viewBox="0 0 24 24" fill="none" stroke="#fff" stroke-width="1.6"><path d="M12 3v18M3 12h18M6 6l12 12M18 6L6 18"/></svg></div><h3>Mulch/<br>Bark Installation</h3><div class="thumb" role="img" aria-label="Worker in yellow spreading bark mulch in a garden bed" style="background:linear-gradient(180deg,#4f6b35,#6b4a2e)"></div></div>
<div class="service-card" style="left:765px;top:1539px"><div class="icon-circle abs ic"><svg width="30" height="30" viewBox="0 0 24 24" fill="none" stroke="#fff" stroke-width="1.6"><circle cx="14" cy="8" r="5"/><path d="M14 13v8M4 21h16M6 14l4 3"/></svg></div><h3>Tree Services &amp;<br>Shrub Pruning</h3><div class="thumb" role="img" aria-label="Arborist climbing a tall pine tree against blue sky" style="background:linear-gradient(180deg,#4f8fd0,#7a5a3a)"></div></div>

<div class="btn" style="left:558px;top:1822px;width:83px;height:30px">View All</div>
<svg class="abs" style="left:0;top:1895px" width="1200" height="85" viewBox="0 0 1200 85">
  <path d="M0 5 C 200 60, 380 80, 620 55 S 1000 15, 1200 30 L1200 85 L0 85Z" fill="url(#waveBlue)"/>
  <path d="M0 25 C 200 82, 420 85, 660 66 S 1020 35, 1200 75 L1200 85 L0 85Z" fill="#fff"/>
</svg>

<!-- testimonials -->
<h2 class="h2" style="top:2040px">Testimonials</h2>
<div class="icon-circle abs quote"><svg width="28" height="24" viewBox="0 0 28 24" fill="#fff"><path d="M2 4h9v9l-4 9H3l3-9H2zM16 4h9v9l-4 9h-4l3-9h-4z"/></svg></div>
<div class="abs stars">★★★★★</div>
<div class="abs t-title">THANK YOU FOR COMING ON SUCH SHORT NOTICE!</div>
<div class="abs t-body">Thank You For Coming On Such Short Notice To Take Down My 60 Foot Oak Tree That Had Been Hit By Lightning.<br>It Is This Level Of Customer Service That Will Keep Me Coming Back.</div>
<svg class="arrow" style="left:200px" width="14" height="20" viewBox="0 0 14 20"><path d="M10 3L3 10l7 7" stroke="var(--green)" stroke-width="2" fill="none"/></svg>
<svg class="arrow" style="left:984px" width="14" height="20" viewBox="0 0 14 20"><path d="M4 3l7 7-7 7" stroke="var(--blue)" stroke-width="2" fill="none"/></svg>
<div class="abs" style="left:514px;top:2284px;width:50px;height:50px;border-radius:50%;border:2px solid var(--green);padding:3px"><div role="img" aria-label="Customer portrait" style="width:100%;height:100%;border-radius:50%;background:#c9a58a"></div></div>
<div class="abs" style="left:571px;top:2296px"><div style="font:600 12px 'Lexend',sans-serif;color:#1e4f8f">Dale,</div><div style="font:400 9.5px 'Poppins',sans-serif;color:#888">Northeast Maple Falls</div></div>

<!-- blogs -->
<section class="abs band" style="top:2409px;height:640px" role="img" aria-label="Darkened photo of a garden path"></section>
<h2 class="h2" style="top:2474px">Our Blogs</h2>

<article class="blog-card" style="left:157px"><div class="thumb" role="img" aria-label="Manicured lawn with rounded shrubs" style="background:linear-gradient(180deg,#6c9a4a,#5fae35)"></div><div class="icon-circle abs date">Oct 11<b>2016</b></div><h3>Good grass in the spring starts with fertilizer in the fall</h3><p>One of the most common questions we get from our customers is what...</p></article>
<article class="blog-card" style="left:460px"><div class="thumb" role="img" aria-label="Blue house with flowering tree and landscaped walkway" style="background:linear-gradient(180deg,#8fb3de,#5c7a94 55%,#6aa043)"></div><div class="icon-circle abs date">Sep 25<b>2016</b></div><h3>Now is the time to plan for your spring garden &amp; landscaping</h3><p>As the cool weather starts to set in, it can be a hard time for garden fans!...</p></article>
<article class="blog-card" style="left:765px"><div class="thumb" role="img" aria-label="Garden with pond and trees under a blue tint" style="background:linear-gradient(135deg,#2f9a8a,#4a86c8 50%,#3d6fae)"></div><div class="icon-circle abs" style="left:18px;top:133px;width:66px;height:66px;background:var(--blue);border:4px solid #fff"><svg width="26" height="26" viewBox="0 0 24 24" fill="none" stroke="#fff" stroke-width="1.8"><path d="M5 4l15 8-15 8 4-8z"/></svg></div><h3 style="color:var(--blue)">Why late summer is the perfect time for our tree service</h3><p>Larch Hollow Landscaping is busy helping our clients prepare their trees for the...</p></article>

<div class="btn" style="left:558px;top:2880px;width:83px;height:31px">View All</div>
<svg class="abs" style="left:0;top:2968px" width="1200" height="85" viewBox="0 0 1200 85">
  <path d="M0 5 C 200 60, 380 80, 620 55 S 1000 15, 1200 30 L1200 85 L0 85Z" fill="url(#waveBlue)"/>
  <path d="M0 25 C 200 82, 420 85, 660 66 S 1020 35, 1200 75 L1200 85 L0 85Z" fill="#fff"/>
</svg>

<!-- inquiry -->
<h2 class="h2" style="top:3112px">Quick Inquiry</h2>
<div class="abs" style="left:0;top:3153px;width:1200px;text-align:center;font:500 12px 'Poppins',sans-serif">Contact Us today, &amp; get reply with in 24 hours!</div>
<form>
  <div class="field" style="left:326px;top:3192px;width:268px;height:32px">First Name</div>
  <div class="field" style="left:607px;top:3192px;width:268px;height:32px">Last Name</div>
  <div class="field" style="left:326px;top:3241px;width:268px;height:32px">Email</div>
  <div class="field" style="left:607px;top:3241px;width:268px;height:32px">Phone</div>
  <div class="field" style="left:326px;top:3290px;width:549px;height:78px">How Can We Help?</div>
  <div class="btn" style="left:562px;top:3397px;width:76px;height:31px">Submit</div>
</form>

<!-- footer -->
<footer class="abs footer" role="img" aria-label="Darkened photo of a garden"></footer>
<div class="abs footer-logo"><span class="wordmark" style="font-size:28px">Larch Hollow</span></div>

<div class="f-item" style="left:172px"><svg width="20" height="20" viewBox="0 0 24 24" fill="var(--green)"><path d="M6.6 10.8a15 15 0 006.6 6.6l2.2-2.2c.3-.3.7-.4 1-.2 1.1.4 2.3.6 3.6.6.6 0 1 .4 1 1V20c0 .6-.4 1-1 1A17 17 0 013 4c0-.6.4-1 1-1h3.5c.6 0 1 .4 1 1 0 1.3.2 2.5.6 3.6.1.3 0 .7-.2 1z"/></svg><div><small>Call Now</small><b>(555) 214-7380</b></div></div>
<div class="f-item" style="left:316px"><svg width="22" height="20" viewBox="0 0 24 22" fill="var(--green)"><path d="M2 8l10-6 10 6v12H2z"/><path d="M2 8l10 7 10-7" stroke="#152219" stroke-width="1.5" fill="none"/></svg><div><small>Email</small><b>hello@larchhollow.com</b></div></div>
<div class="f-item" style="left:556px"><svg width="16" height="22" viewBox="0 0 16 22" fill="var(--green)"><path d="M8 0a8 8 0 018 8c0 6-8 14-8 14S0 14 0 8a8 8 0 018-8z"/><circle cx="8" cy="8" r="3" fill="#152219"/></svg><div><small>Address</small><b>1840 Birchwood Ridge Dr SE<br>Maple Falls, MI 49500</b></div></div>
<div class="f-item" style="left:780px"><svg width="20" height="20" viewBox="0 0 24 24" fill="none" stroke="var(--green)" stroke-width="2"><path d="M3 5l6-2 6 2 6-2v16l-6 2-6-2-6 2z"/><path d="M9 3v16M15 5v16"/></svg><div><small>Live</small><b style="text-decoration:underline">Location</b></div></div>
<div class="abs" style="left:982px;top:3652px;width:26px;height:26px;border-radius:50%;background:#2c3a30;border:1px solid #556"></div>
<div class="abs" style="left:1018px;top:3652px;width:26px;height:26px;border-radius:50%;background:var(--green)"></div>

<nav class="f-nav">
  <a style="left:418px;color:var(--green);text-decoration:underline">Home</a>
  <a style="left:478px">About Us</a>
  <a style="left:555px">Services</a>
  <a style="left:631px">Testimonials</a>
  <a style="left:725px">Contact Us</a>
</nav>
<div class="abs bottom-bar"><span class="abs" style="left:157px;top:14px">© 2025 Larch Hollow Landscaping, All rights reserved</span><span class="abs" style="left:971px;top:14px">Privacy Policy</span></div>

</div>
</body>
</html>
```